Commercial Business Card - stand out, clean, simple, unique.

commercial real estate group located in Texas. Called 4 Ridges Real Estate. We want a unique yet clean and professional card. On one side I would like the 4R to be by itself or to look as unique or tasteful as possible. We have the logo in white, black, and color in case a black background or something similar looks best on one side. We need a space for our name, email, cell. website. And possibly room for a phrase or city.

Contact Information for Business Card

Name, Title, Email, Phone Number, website

```html
<!DOCTYPE html>
<html lang="en">
<head>
<meta charset="utf-8">
<title>4 Ridges Real Estate – Business Card</title>
<link href="https://fonts.googleapis.com/css2?family=Open+Sans:ital,wght@0,400;0,700;1,400&display=swap" rel="stylesheet">
<style>
  :root {
    --page: #e9e6e1;
    --card: #343434;
    --card-back: #3d3d3d;
    --brand-blue: #6f86e6;
    --ink: #ffffff;
    --ink-soft: #d6d6d6;
  }
  * { box-sizing: border-box; margin: 0; padding: 0; }
  html, body {
    width: 1200px; height: 1200px; overflow: hidden;
    background: var(--page);
    font-family: "Open Sans", Arial, sans-serif;
  }
  .sheet {
    width: 1200px; height: 1200px;
    display: flex; flex-direction: column; align-items: center; justify-content: center;
    gap: 26px;
  }
  .card {
    position: relative;
    width: 960px; height: 549px;
    border-radius: 6px;
    box-shadow: 0 10px 26px rgba(0,0,0,0.22);
  }
  .card--back { background: var(--card-back); display: flex; align-items: center; justify-content: center; }
  .card--front { background: var(--card); }

  .wordmark { display: flex; align-items: center; gap: 20px; }
  .wordmark__square { flex: none; width: 24px; height: 24px; background: var(--brand-blue); }
  .wordmark__name {
    font-weight: 700; color: var(--brand-blue);
    font-size: 44px; line-height: 1; letter-spacing: 2px; text-transform: uppercase;
    white-space: nowrap;
  }
  .card--front .wordmark { position: absolute; left: 84px; top: 80px; }
  .card--front .wordmark__name { font-size: 48px; }

  .contact {
    position: absolute; left: 84px; bottom: 70px; right: 60px;
    color: var(--ink);
  }
  .contact__who { display: flex; align-items: baseline; gap: 22px; margin-bottom: 16px; }
  .contact__name { font-weight: 700; font-size: 30px; letter-spacing: 0.5px; }
  .contact__title { font-style: italic; font-size: 22px; color: var(--ink-soft); }
  .contact__lines { display: flex; align-items: baseline; gap: 22px; font-size: 21px; color: var(--ink-soft); white-space: nowrap; }
  .sep { color: var(--ink); font-size: 24px; }
</style>
</head>
<body>
  <main class="sheet">
    <section class="card card--back" aria-label="Card back">
      <div class="wordmark">
        <span class="wordmark__square"></span>
        <span class="wordmark__name">4 Ridges Real Estate</span>
      </div>
    </section>

    <section class="card card--front" aria-label="Card front">
      <div class="wordmark">
        <span class="wordmark__square"></span>
        <span class="wordmark__name">4 Ridges Real Estate</span>
      </div>

      <div class="contact">
        <div class="contact__who">
          <span class="contact__name">DANA HOLLIS</span>
          <span class="sep">|</span>
          <span class="contact__title">Manager</span>
        </div>
        <div class="contact__lines">
          <span class="contact__phone">+1 (555) 014 - 2270</span>
          <span class="sep">|</span>
          <span class="contact__email">dana@ridgesmail.net</span>
          <span class="sep">|</span>
          <span class="contact__web">www.fourridgesexample.com</span>
        </div>
      </div>
    </section>
  </main>
</body>
</html>
```